Corporate Design für Steuerberatung
Zielgruppe
Wir sind eine junge Steuerkanzlei und möchten mit hochwertigem, modernem und zeitlosem Design überzeugen. Der Mandantenstamm ist vielfältig, und erstreckt sich über ein Alter von 20 Jahre bis hin zu 75 Jahre.
Aufgabenstellung
Das Design soll möglichst schnörkellos sein, modern aber gleichzeitig auch klassisch und zeitlos. Eher exklusiv und 'maskulin' gehalten.
Die Buchstaben tbr können klein oder in Großbuchstaben geschrieben werden, auch mit Strichen, Punkten oder anderen Formen von einander getrennt sein.

```html
<!DOCTYPE html>
<html lang="de">
<head>
<meta charset="utf-8">
<title>TBR Steuerberatung – Corporate Design</title>
<link href="https://fonts.googleapis.com/css2?family=Montserrat:wght@300;400;500;600&display=swap" rel="stylesheet">
<style>
  :root {
    --brand-blue: #5570b2;
    --text-grey: #6a6a6e;
    --top-bg: #f8f8f8;
    --stage-bg: #e4e4e4;
    --sheet-bg: #b3b3b3;
    --paper: #ffffff;
  }
  * { margin: 0; padding: 0; box-sizing: border-box; }
  html, body { width: 1200px; height: 2644px; overflow: hidden; }
  body { position: relative; font-family: "Montserrat", sans-serif; color: var(--text-grey); background: var(--top-bg); }

  .section { position: absolute; left: 0; width: 1200px; }
  .section--logo { top: 0; height: 518px; background: var(--top-bg); }
  .section--cards { top: 518px; height: 796px; background: var(--stage-bg); }
  .section--letter { top: 1314px; height: 1330px; background: var(--sheet-bg); }

  /* wordmark */
  .wordmark { position: absolute; display: flex; align-items: center; }
  .wordmark__square { background: var(--brand-blue); flex: none; }
  .wordmark__name { color: var(--brand-blue); font-weight: 500; line-height: 1; }
  .wordmark__tagline { position: absolute; font-weight: 300; text-transform: uppercase; color: var(--text-grey); white-space: nowrap; }

  .hero-mark { left: 372px; top: 142px; height: 142px; }
  .hero-mark .wordmark__square { width: 142px; height: 142px; }
  .hero-mark .wordmark__name { font-size: 150px; letter-spacing: 26px; margin-left: 34px; }
  .hero-tagline { left: 372px; top: 300px; font-size: 32px; letter-spacing: 17.6px; }

  /* business cards */
  .card { position: absolute; top: 140px; width: 330px; height: 510px; box-shadow: 0 10px 24px rgba(0,0,0,.22); }
  .card--front { left: 215px; background: var(--paper); }
  .card--back { left: 655px; background: var(--brand-blue); }
  .card .wordmark { left: 34px; top: 44px; height: 58px; }
  .card .wordmark__square { width: 58px; height: 58px; }
  .card .wordmark__name { font-size: 60px; letter-spacing: 10px; margin-left: 14px; }
  .card-tagline { left: 34px; top: 112px; font-size: 13px; letter-spacing: 7.4px; }
  .smallcaps { font-variant: small-caps; text-transform: lowercase; letter-spacing: 1.4px; }
  .card__person { position: absolute; right: 34px; top: 180px; text-align: right; }
  .card__name { color: var(--brand-blue); font-weight: 600; font-size: 17px; line-height: 22px; }
  .card__role { font-size: 13px; line-height: 18px; }
  .card__contact { position: absolute; left: 34px; top: 300px; font-size: 13px; line-height: 19px; }
  .card__contact .gap { height: 12px; }
  .card__contact .label { display: inline-block; width: 78px; }

  /* letterhead */
  .letter { position: absolute; left: 200px; top: 87px; width: 801px; height: 1132px; background: var(--paper); box-shadow: 0 8px 22px rgba(0,0,0,.3); }
  .letter .wordmark { right: 27px; top: 33px; height: 54px; }
  .letter .wordmark__square { width: 54px; height: 54px; }
  .letter .wordmark__name { font-size: 52px; letter-spacing: 8px; margin-left: 14px; margin-right: -8px; }
  .letter-tagline { right: 27px; top: 96px; font-size: 12.5px; letter-spacing: 5.4px; margin-right: -5.4px; }
  .letter__team { position: absolute; right: 27px; top: 140px; text-align: right; font-size: 9.5px; line-height: 12.4px; letter-spacing: 1.2px; }
  .letter__team .lead { color: var(--brand-blue); font-weight: 600; }
  .letter__team .gap { height: 8.5px; }
  .letter__sender { position: absolute; left: 62px; top: 215px; font-size: 6.5px; letter-spacing: .6px; }
  .fold-mark { position: absolute; left: 8px; width: 11px; height: 1px; background: #8a8a8a; }
  .fold-mark--upper { top: 396px; }
  .fold-mark--lower { top: 797px; }
  .letter__bank { position: absolute; right: 27px; bottom: 34px; text-align: right; font-size: 7.5px; line-height: 11px; letter-spacing: .8px; }
  .letter__bank .lead { color: var(--brand-blue); font-weight: 600; }
</style>
</head>
<body>

<section class="section section--logo">
  <div class="wordmark hero-mark">
    <span class="wordmark__square"></span>
    <span class="wordmark__name">TBR</span>
  </div>
  <div class="wordmark__tagline hero-tagline">Steuerberatung</div>
</section>

<section class="section section--cards">
  <article class="card card--front">
    <div class="wordmark">
      <span class="wordmark__square"></span>
      <span class="wordmark__name">TBR</span>
    </div>
    <div class="wordmark__tagline card-tagline">Steuerberatung</div>
    <div class="card__person smallcaps">
      <div class="card__name">Hans Mustermann</div>
      <div class="card__role">Steuerberater</div>
      <div class="card__role">Wirtschaftsprüfer</div>
    </div>
    <div class="card__contact smallcaps">
      <div>TBR Steuerberater GmbH</div>
      <div>Beispielstrasse 123</div>
      <div>54321 Musterstadt</div>
      <div class="gap"></div>
      <div><span class="label">Telefon:</span>+49 (0) 123 456 789 01</div>
      <div><span class="label">Telefax:</span>+49 (0) 123 456 789 02</div>
      <div class="gap"></div>
      <div><span class="label">E-Mail:</span>info@tbrberater.eu</div>
      <div><span class="label">Internet:</span>www.tbrberater.eu</div>
    </div>
  </article>
  <article class="card card--back" aria-label="Kartenrückseite"></article>
</section>

<section class="section section--letter">
  <article class="letter">
    <div class="wordmark">
      <span class="wordmark__square"></span>
      <span class="wordmark__name">TBR</span>
    </div>
    <div class="wordmark__tagline letter-tagline">Steuerberatung</div>

    <div class="letter__team smallcaps">
      <div class="lead">Hans Mustermann</div>
      <div>Steuerberater . Wirtschaftsprüfer</div>
      <div class="gap"></div>
      <div class="lead">Michael Beispielhaft</div>
      <div>Steuerberater</div>
      <div class="gap"></div>
      <div class="lead">Werner Wichtig</div>
      <div>Steuer- und Anlageberater</div>
      <div class="gap"></div>
      <div>Beispielstrasse 123</div>
      <div>54321 Musterstadt</div>
      <div class="gap"></div>
      <div>E-Mail: info@tbrberatung.eu</div>
      <div>Internet: www.tbrberatung.eu</div>
    </div>

    <div class="letter__sender smallcaps">TBR Steuerberatung . Beispielstrasse 123 . 54321 Musterstadt</div>

    <span class="fold-mark fold-mark--upper"></span>
    <span class="fold-mark fold-mark--lower"></span>

    <div class="letter__bank smallcaps">
      <div class="lead">Bankverbindung</div>
      <div>Deutsche Beispielbank</div>
      <div>BIC: DEBEIBA0007</div>
      <div>IBAN: DE14 1234 0000 5678 9101 23</div>
    </div>
  </article>
</section>

</body>
</html>
```